Motivational Quotes Poster Series

This is a 3 poster design series for Ridgeway Haul Academy. The size of each poster should be 18 inches wide and 24 inches tall. The goal of these posters is to serve as motivational "signs" to be hung in the office area for the employees (not customers). These employees are instructors/teachers, teaching students how to drive semi trucks. While each design is a separate poster and design, we're posting as 1 project because we'd like some continuity between the series. Below we'll break down the details of all 3 posters...

Poster #1
Text that must appear on poster - "If You Want The Best Out Of Each Student" and "Give The Best Of You!" Note: While this text must appear on the poster, you can arrange in the layout as you see fit. For example, first line could be at top of poster and second line on bottom.

Poster #2
Text that must appear on poster - "Invest In People" and "Change Someone's Life" (same notes apply as in 1st poster)

Poster #3
Text that must appear on poster - "Today Is..." and "Just Another Day For You" and "The Most Important Day In Their Life" Note: This can be laid out on the poster however you see fit, but each phrase needs to be separate and it needs to flow.

Target Market(s)

Truck Driver Training Instructors - These are middle-aged, mostly male, masculine type personalities.

Industry/Entity Type

Training

Requirements
Must have
• Must have noted text from description
Must have working files (ie - PSD, EPS, AI, etc) provided
Must have common theme between each poster in series
Must have easy to read font and layout
Must have product dimensions of 18 inches (width) by 24 inches (height). If design uses full dimensions please include quarter inch bleed.
Nice to have
• Nice to have a trucking theme...related to trucking industry, but not over the top. Example - This could mean subtle injection of background tire tracks, but by no means are tire tracks required.

For inspiration, you can visit the site at http://www.ridgewayhaul.example. While you can use the colors of the site/logo, you can still branch out between each poster to try new colors within reason.

Note: While we've attached the logo to this project, it COULD be used but doesn't HAVE to be included in the design. The logo IS NOT a focal point. The phrases in the poster ARE the focal point.

```html
<!DOCTYPE html>
<html lang="en">
<head>
<meta charset="utf-8">
<title>Give The Best Of You — Motivational Poster</title>
<link href="https://fonts.googleapis.com/css2?family=Black+Ops+One&display=swap" rel="stylesheet">
<style>
  :root {
    --teal-glow: #23b3c4;
    --ocean: #0d5f93;
    --deep-navy: #0a2147;
    --night: #050f24;
    --quote-yellow: #ffe000;
    --quote-white: #ffffff;
    --type-shadow: #0b2340;
    --stripe-green: #8cd24a;
    --stripe-olive: #9aa63a;
    --stripe-rust: #c44a22;
  }
  html, body {
    margin: 0;
    padding: 0;
    width: 900px;
    height: 1200px;
    overflow: hidden;
    background: var(--night);
  }
  .poster {
    position: relative;
    width: 900px;
    height: 1200px;
    overflow: hidden;
    background:
      radial-gradient(ellipse 60% 45% at 15% 40%, var(--teal-glow) 0%, rgba(35,179,196,0) 70%),
      radial-gradient(ellipse 70% 60% at 55% 50%, var(--ocean) 0%, rgba(13,95,147,0) 80%),
      linear-gradient(180deg, #0e4f7a 0%, #106a98 35%, #0c4d86 65%, var(--deep-navy) 100%);
  }
  .poster::after {
    content: "";
    position: absolute;
    inset: 0;
    background: radial-gradient(ellipse 80% 75% at 45% 45%, rgba(0,0,0,0) 55%, rgba(3,10,28,0.75) 100%);
    pointer-events: none;
  }
  .poster-art {
    position: absolute;
    inset: 0;
    z-index: 1;
  }
  .quote-line {
    font-family: "Black Ops One", "Arial Black", sans-serif;
    text-transform: uppercase;
  }
  .quote-line--accent { fill: var(--quote-yellow); }
  .quote-line--plain { fill: var(--quote-white); }
  .quote-block {
    filter: drop-shadow(5px 5px 0 var(--type-shadow));
  }
</style>
</head>
<body>
  <main class="poster">
    <svg class="poster-art" width="900" height="1200" viewBox="0 0 900 1200" xmlns="http://www.w3.org/2000/svg">
      <defs>
        <linearGradient id="stripe-tone" x1="0" y1="0" x2="900" y2="0" gradientUnits="userSpaceOnUse">
          <stop offset="0" stop-color="var(--stripe-green)"/>
          <stop offset="0.5" stop-color="var(--stripe-green)"/>
          <stop offset="0.72" stop-color="var(--stripe-olive)"/>
          <stop offset="1" stop-color="var(--stripe-rust)"/>
        </linearGradient>
      </defs>

      <g class="hazard-band" fill="url(#stripe-tone)" opacity="0.82">
        <polygon points="-30,692 30,692 90,522 30,522"/>
        <polygon points="82,692 144,692 204,522 142,522"/>
        <polygon points="194,692 256,692 316,522 254,522"/>
        <polygon points="306,692 368,692 428,522 366,522"/>
        <polygon points="418,692 480,692 540,522 478,522"/>
        <polygon points="530,692 592,692 652,522 590,522"/>
        <polygon points="642,692 704,692 764,522 702,522"/>
        <polygon points="754,692 816,692 876,522 814,522"/>
        <polygon points="866,692 928,692 988,522 926,522"/>
      </g>

      <g class="quote-block quote-block--ask">
        <text class="quote-line quote-line--accent" x="145" y="130" font-size="130" textLength="100" lengthAdjust="spacingAndGlyphs">If</text>
        <text class="quote-line quote-line--plain" x="178" y="214" font-size="100" textLength="462" lengthAdjust="spacingAndGlyphs">You Want</text>
        <text class="quote-line quote-line--accent" x="45" y="335" font-size="168" textLength="755" lengthAdjust="spacingAndGlyphs">The Best</text>
        <text class="quote-line quote-line--plain" x="108" y="414" font-size="96" textLength="627" lengthAdjust="spacingAndGlyphs">Out Of Each</text>
        <text class="quote-line quote-line--accent" x="290" y="514" font-size="138" textLength="570" lengthAdjust="spacingAndGlyphs">Student</text>
      </g>

      <g class="quote-block quote-block--answer">
        <text class="quote-line quote-line--plain" x="200" y="818" font-size="165" textLength="365" lengthAdjust="spacingAndGlyphs">Give</text>
        <text class="quote-line quote-line--accent" x="95" y="914" font-size="130" textLength="600" lengthAdjust="spacingAndGlyphs">The Best</text>
        <text class="quote-line quote-line--plain" x="340" y="1008" font-size="118" textLength="140" lengthAdjust="spacingAndGlyphs">Of</text>
        <text class="quote-line quote-line--accent" x="340" y="1168" font-size="205" textLength="385" lengthAdjust="spacingAndGlyphs">You</text>
      </g>
    </svg>
  </main>
</body>
</html>
```